Tessa Lane Staging & Design - a company built on first impressions, needs an impressive letterhead

Please create a letter head to be used for our project proposals, contract agreements and other client correspondence. We are a home Staging and interior design company. We like sleek, modern, clean and elegant design. Please create a document that compliments and uses our logo. We will also be creating flyers that we would like to match our letterhead and future marketing materials

Target Market(s)

real estate agents, home owners looking to sell

Industry/Entity Type

Interior Design

```html
<!DOCTYPE html>
<html lang="en">
<head>
<meta charset="utf-8">
<title>Tessa Lane Staging &amp; Design — Letterhead</title>
<link href="https://fonts.googleapis.com/css2?family=Montserrat:wght@400&display=swap" rel="stylesheet">
<style>
  :root {
    --backdrop: #d6d6d6;
    --paper: #f7f7f7;
    --ink: #1e1e1e;
    --ink-soft: #5a5a5a;
  }
  * { box-sizing: border-box; margin: 0; padding: 0; }
  html, body {
    width: 1200px;
    height: 780px;
    overflow: hidden;
    background: var(--backdrop);
  }
  .letterhead {
    position: absolute;
    left: 345px;
    top: 30px;
    width: 510px;
    height: 720px;
    background: var(--paper);
    font-family: "Montserrat", sans-serif;
  }
  .brand {
    position: absolute;
    left: 39px;
    top: 68px;
    font-weight: 400;
    font-size: 10.5px;
    line-height: 1.55;
    letter-spacing: 1.2px;
    text-transform: uppercase;
    color: var(--ink-soft);
  }
  .contact {
    position: absolute;
    top: 75px;
    left: 293px;
    display: flex;
    gap: 9px;
    font-size: 6.6px;
    line-height: 9px;
    color: var(--ink);
  }
  .contact-address p { white-space: nowrap; }
  .contact-list { list-style: none; }
  .contact-list li {
    display: flex;
    align-items: center;
    gap: 4px;
    white-space: nowrap;
  }
  .contact-icon {
    width: 6px;
    height: 6px;
    flex: none;
  }
</style>
</head>
<body>
  <main class="letterhead">
    <header>
      <div class="brand">Tessa Lane<br>Staging &amp; Design</div>
      <div class="contact">
        <address class="contact-address" style="font-style:normal">
          <p>48 Alder Grove Lane</p>
          <p>Maple Heights, CA 90412</p>
        </address>
        <ul class="contact-list">
          <li>
            <svg class="contact-icon" viewBox="0 0 10 10" aria-hidden="true"><path d="M2 1 L4 1 L4.6 3.4 L3.4 4.2 Q4.4 6 6 6.8 L6.8 5.6 L9 6.2 L9 8.2 Q8.8 9 8 9 Q1 8.6 1 2 Q1 1 2 1 Z" fill="var(--ink)"/></svg>
            <span>+1 555 014 2290</span>
          </li>
          <li>
            <svg class="contact-icon" viewBox="0 0 10 10" aria-hidden="true"><circle cx="5" cy="5" r="5" fill="var(--ink)"/><rect x="2.4" y="3.2" width="5.2" height="3.6" fill="none" stroke="var(--paper)" stroke-width="0.8"/><path d="M2.4 3.2 L5 5.2 L7.6 3.2" fill="none" stroke="var(--paper)" stroke-width="0.8"/></svg>
            <span>hello@tessalanestaging.com</span>
          </li>
          <li>
            <svg class="contact-icon" viewBox="0 0 10 10" aria-hidden="true"><circle cx="5" cy="5" r="5" fill="var(--ink)"/><circle cx="5" cy="5" r="2.8" fill="none" stroke="var(--paper)" stroke-width="0.7"/><path d="M2.2 5 H7.8 M5 2.2 Q3.4 5 5 7.8 M5 2.2 Q6.6 5 5 7.8" fill="none" stroke="var(--paper)" stroke-width="0.6"/></svg>
            <span>www.tessalanestaging.com</span>
          </li>
        </ul>
      </div>
    </header>
  </main>
</body>
</html>
```